Finance Broker helping people meet their personal and business goals

New business card design,
1st look at the old business card so this makes sense.
I DON'T want:
the subtext "For all your Rural and Commercial Finance".
I DON'T want the: "and Management Consultant" words
I DON'T want the old phone: 07 48213957
I DON'T want the fax number: 07 45826031
I DON'T want the email address: tallowcreek@brightlink.com.au
I DON'T want the flower
What I DO want
I DO want the mobile 0451 836 209 (in larger text)
I DO want:
My name: Dennis Harwell-Lowe
I DO want: Australian Credit Licence 529164 (Tallow Creek Pty Ltd)
I DO want: Principal Finance Broker
I DO want new email: dennis@plotnextstep.com.au
I DO want address: PO Box 928, Tully Qld 4854
I DO want the existing logo (PNS on existing card)

Target Market(s)

Business Borrowers, Home Purchasers, and People wanting to finance cars and plant and equipment

Industry/Entity Type

Financial Service

Contact Information for Business Card

See project description

Font styles to use
Serif

Colors

Designer to choose colors to be used in the design.

Requirements
Must have
• See project description
Nice to have
• Black and Yellow colours
Should not have
• See project description

```html
<!DOCTYPE html>
<html lang="en">
<head>
<meta charset="utf-8">
<title>Plot Next Step – Business Card</title>
<link rel="stylesheet" href="https://fonts.googleapis.com/css2?family=Tinos:wght@400;700&family=Open+Sans:wght@400&display=swap">
<style>
  :root {
    --backdrop: #2b2b2b;
    --card: #121212;
    --accent: #e6ea72;
    --ink-light: #f2f2f2;
    --ink-dark: #111111;
  }
  * { margin: 0; padding: 0; box-sizing: border-box; }
  html, body { width: 1200px; height: 900px; overflow: hidden; }
  body {
    background: var(--backdrop);
    font-family: "Tinos", "Times New Roman", serif;
    display: flex;
    flex-direction: column;
    align-items: center;
    justify-content: center;
    gap: 40px;
  }
  .card {
    position: relative;
    width: 700px;
    height: 400px;
    background: var(--card);
    border-radius: 18px;
    overflow: hidden;
    box-shadow: 0 10px 30px rgba(0,0,0,.45);
  }
  .brand {
    display: flex;
    flex-direction: column;
    align-items: flex-start;
  }
  .brand-row { display: flex; align-items: center; gap: 14px; }
  .brand-name {
    font-family: "Tinos", serif;
    font-weight: 700;
    color: var(--accent);
    font-size: 40px;
    line-height: 1;
  }
  .brand-dot {
    width: 40px; height: 40px; border-radius: 50%;
    background: var(--accent);
  }
  .brand-tagline {
    font-family: "Open Sans", sans-serif;
    color: var(--ink-light);
    font-size: 15px;
    letter-spacing: .3px;
    margin-top: 6px;
    margin-left: 4px;
  }
  /* front */
  .card-front .brand {
    position: absolute;
    left: 50%; top: 50%;
    transform: translate(-50%, -50%);
  }
  /* back */
  .card-back .brand {
    position: absolute;
    left: 50%; top: 48px;
    transform: translateX(-46%);
  }
  .name-band {
    position: absolute;
    left: 0; right: 0; top: 150px;
    height: 58px;
    background: var(--accent);
    display: flex;
    align-items: center;
    justify-content: center;
    gap: 16px;
    color: var(--ink-dark);
  }
  .person-name { font-weight: 700; font-size: 31px; }
  .band-divider { font-weight: 700; font-size: 26px; }
  .person-title { font-size: 18px; }
  .details {
    position: absolute;
    left: 0; right: 0; top: 222px;
    display: flex;
    flex-direction: column;
    align-items: center;
    color: var(--ink-light);
  }
  .licence { font-size: 16px; }
  .rule { width: 34px; height: 2px; background: var(--accent); margin: 12px 0 10px; }
  .contact { display: flex; align-items: center; gap: 8px; }
  .contact svg { fill: var(--ink-light); }
  .contact-phone { font-size: 30px; margin-bottom: 10px; }
  .contact-email, .contact-address { font-size: 16px; margin-bottom: 6px; }
</style>
</head>
<body>
  <section class="card card-front" aria-label="Card front">
    <div class="brand">
      <div class="brand-row">
        <span class="brand-name">Plot Next Step</span>
        <span class="brand-dot"></span>
      </div>
      <span class="brand-tagline">A Member of the Tallow Creek Group</span>
    </div>
  </section>

  <section class="card card-back" aria-label="Card back">
    <div class="brand">
      <div class="brand-row">
        <span class="brand-name">Plot Next Step</span>
        <span class="brand-dot"></span>
      </div>
      <span class="brand-tagline">A Member of the Tallow Creek Group</span>
    </div>

    <div class="name-band">
      <span class="person-name">Dennis Harwell-Lowe</span>
      <span class="band-divider">|</span>
      <span class="person-title">Principal Finance Broker</span>
    </div>

    <div class="details">
      <p class="licence">Australian Credit Licence 529164 (Tallow Creek Pty Ltd)</p>
      <span class="rule"></span>
      <p class="contact contact-phone">
        <svg width="18" height="18" viewBox="0 0 24 24" aria-hidden="true"><path d="M6.6 10.8c1.4 2.8 3.8 5.1 6.6 6.6l2.2-2.2c.3-.3.7-.4 1-.2 1.1.4 2.3.6 3.6.6.6 0 1 .4 1 1V20c0 .6-.4 1-1 1C10.6 21 3 13.4 3 4c0-.6.4-1 1-1h3.5c.6 0 1 .4 1 1 0 1.3.2 2.5.6 3.6.1.3 0 .7-.2 1l-2.3 2.2z"/></svg>
        0451 836 209
      </p>
      <p class="contact contact-email">
        <svg width="16" height="16" viewBox="0 0 24 24" aria-hidden="true"><path d="M2 5h20v14H2z M4 7v.4l8 5 8-5V7z" fill-rule="evenodd"/></svg>
        dennis@plotnextstep.com.au
      </p>
      <p class="contact contact-address">
        <svg width="14" height="16" viewBox="0 0 24 24" aria-hidden="true"><path d="M12 2a7 7 0 0 0-7 7c0 5 7 13 7 13s7-8 7-13a7 7 0 0 0-7-7zm0 9.5A2.5 2.5 0 1 1 12 6.5a2.5 2.5 0 0 1 0 5z"/></svg>
        PO Box 928, Tully Qld 4854
      </p>
    </div>
  </section>
</body>
</html>
```